Engineering Consultant Business Card

I'm starting a new business as a high-end engineering consultant in a niche field. I've attached the jpg for my logo plus the branding guideline document that I've been following. You can see my business website here: www.tarvikworks.com
I'd like a business card that has the logo on one side, then the other side has (in any order): Tarvik Works, Inc.
Dana Whitlock
President and Chief EMC Engineer
www.tarvikworks.com
dana@tarvikworks.com
Optional: motto "We will solve your EMC problems as early as possible—ideally before they even start."
I'm not planning on including a phone number
Target Market(s)
Businesses, especially makers of electronics hardware
Industry/Entity Type
Electrical engineering
Contact Information for Business Card
Company name, my name, website, email

```html
<!DOCTYPE html>
<html lang="en">
<head>
<meta charset="utf-8">
<title>Tarvik Works, Inc. – Business Card</title>
<link rel="stylesheet" href="https://fonts.googleapis.com/css2?family=Figtree:wght@500;600;700;800&display=swap">
<style>
  :root {
    --backdrop: #8cc2d4;
    --brand-blue: #284899;
    --paper: #ecf7fb;
  }
  * { box-sizing: border-box; margin: 0; padding: 0; }
  html, body {
    width: 1200px;
    height: 1000px;
    overflow: hidden;
    background: var(--backdrop);
    font-family: "Figtree", Arial, sans-serif;
  }
  .card {
    position: absolute;
    left: 316px;
    width: 568px;
    height: 327px;
    overflow: hidden;
  }
  .card--front { top: 127px; background: var(--brand-blue); }
  .card--back { top: 544px; background: var(--paper); }
  .card__arc {
    position: absolute;
    inset: 0;
    width: 100%;
    height: 100%;
  }
  .wordmark {
    position: absolute;
    font-weight: 800;
    font-size: 27px;
    letter-spacing: 0.5px;
    white-space: nowrap;
  }
  .card--front .wordmark {
    left: 125px;
    top: 201px;
    transform: translate(-50%, -50%);
    color: var(--paper);
  }
  .card--back .wordmark {
    left: 486px;
    top: 152px;
    transform: translate(-50%, -50%) rotate(90deg);
    color: var(--brand-blue);
    font-size: 30px;
  }
  .contact {
    position: absolute;
    left: 23px;
    top: 102px;
    color: var(--brand-blue);
  }
  .contact__name {
    font-size: 27px;
    font-weight: 700;
    line-height: 1;
    letter-spacing: -0.2px;
  }
  .contact__title {
    margin-top: 6px;
    font-size: 8.5px;
    font-weight: 600;
    letter-spacing: 1.1px;
    text-transform: uppercase;
  }
  .contact__rule {
    margin-top: 9px;
    width: 226px;
    height: 2px;
    background: var(--brand-blue);
  }
  .contact__links {
    margin-top: 50px;
    list-style: none;
    font-size: 15px;
    font-weight: 500;
    line-height: 26px;
  }
</style>
</head>
<body>
  <section class="card card--front" aria-label="Business card front">
    <svg class="card__arc" viewBox="0 0 568 327" aria-hidden="true">
      <path fill="var(--paper)" d="M0 0 L263 0 C360 80 419 200 419 327 L327 327 C327 150 180 3 0 3 Z"/>
    </svg>
    <div class="wordmark">Tarvik Works</div>
  </section>

  <section class="card card--back" aria-label="Business card back">
    <svg class="card__arc" viewBox="0 0 568 327" aria-hidden="true">
      <path fill="var(--brand-blue)" d="M0 0 L263 0 C360 80 419 200 419 327 L327 327 C327 150 180 3 0 3 Z"/>
    </svg>
    <div class="contact">
      <h1 class="contact__name">Dana Whitlock</h1>
      <p class="contact__title">President and Chief EMC Engineer</p>
      <div class="contact__rule"></div>
      <ul class="contact__links">
        <li>www.tarvikworks.com</li>
        <li>dana@tarvikworks.com</li>
      </ul>
    </div>
    <div class="wordmark">Tarvik Works</div>
  </section>
</body>
</html>
```